Medical Centre Website

We need a new design for a medical centre based in Perth, Western Australia called 'Tarvin Grove Medical Centre'.

The medical centre does general practitioner work including general checkups, ecg, heart checks, woman's health and more servicing children and adults. They also do home visits on occasions where the patient cannot attend the centre.

They would like an information/brochure website where visitors can read up on the practice, send email and view their location.

The client wish the design to be clean, fresh and light. The main colours are a light purple/blue and to a dark navy blue. The client would not want the logo to be altered in any way. This includes changing the words colours or the image.

The final design should represent a loving, family friendly practice where patients can come to receive the best treatments.

We just need the end product to be presented to un in a layed psd format. The fonts must be as per the W3C standards.

**IMPORTANT**
I have received heaps of chatlink invites in the past. To treat everyone fairly, I do not add people to my chatlink list as in the past people expected us to give them the prize. If you have questions, please ask them in pixel forum as it may benefit others who are also designing the site. If I need to, I will send a message to the user.
Updates

Hi Designers,

Most designs we have received have been overly cluttered. Are you able to simplify the designs.

Cheers, Dorian

Hi Designers,

Some of the designs are quite attractive but aremore cluttered than I would like. If you have a look at the following design, the design is very simple and straight to the point. A lot of designs have too much wording and the reader can be put off. We are looking something more like:

velmoxa.com.au

I would prefer to see designs and have opened up the contest for a further 7 days.

Designers,

We have received feedback from the client and Quite frankly he don’t really like any of them.They are too cluttered and Americanised. All drab blue colours.
 
If you have a look at template monster, these designs are better and cleaner. We do not want heaps of writing on the front page.

If you look at the eariler examples such as quorbeyclinic.com.au which I did myself, the client loves that simplicity of the site.

```html
<!DOCTYPE html>
<html lang="en">
<head>
<meta charset="utf-8">
<title>Tarvin Grove Medical Centre</title>
<link href="https://fonts.googleapis.com/css2?family=Source+Sans+3:ital,wght@0,300;0,400;0,600;0,700;1,400&family=Crimson+Text:ital@1&display=swap" rel="stylesheet">
<style>
  :root {
    --brand-blue: #1558a8;
    --link-blue: #1a5fb8;
    --navy-band: #0d5aa7;
    --nav-bg: #3a3a3a;
    --nav-active: #1b63b4;
    --text: #4a4a4a;
    --text-soft: #5c5c5c;
    --tagline: #5d6b2c;
    --white: #ffffff;
    --icon-grey: #444444;
  }
  * { box-sizing: border-box; margin: 0; padding: 0; }
  html, body { width: 922px; height: 1200px; overflow: hidden; background: var(--white); }
  body { font-family: "Source Sans 3", "Helvetica Neue", Arial, sans-serif; color: var(--text); position: relative; }

  .site-header { position: absolute; top: 0; left: 0; width: 922px; height: 143px; }
  .brand { position: absolute; left: 44px; top: 30px; display: flex; align-items: center; gap: 16px; }
  .brand-name { color: var(--brand-blue); font-weight: 400; line-height: 1; }
  .brand-name .line-1 { display: block; font-size: 41px; letter-spacing: -0.2px; }
  .brand-name .line-2 { display: block; font-size: 23px; letter-spacing: 4px; margin-top: 6px; text-align: right; }
  .brand-mark { width: 48px; height: 48px; border-radius: 50%; background: #8ea9d8; }

  .contact-list { position: absolute; right: 20px; top: 20px; text-align: right; }
  .contact-item { display: flex; justify-content: flex-end; align-items: center; gap: 10px; font-size: 14px; font-weight: 700; color: var(--brand-blue); height: 27px; }
  .contact-item svg { flex: none; }
  .hours { display: flex; justify-content: flex-end; align-items: center; gap: 14px; margin-top: 4px; }
  .hours-label { font-size: 19px; font-weight: 600; color: var(--brand-blue); }
  .hours-today { background: var(--navy-band); color: var(--white); font-size: 14px; font-weight: 600; padding: 5px 8px; letter-spacing: 0.2px; }

  .main-nav { position: absolute; top: 143px; left: 0; width: 922px; height: 43px; background: var(--nav-bg); display: flex; align-items: center; }
  .nav-links { display: flex; height: 100%; margin-left: 36px; list-style: none; }
  .nav-links li { display: flex; align-items: center; padding: 0 13px; color: var(--white); font-size: 14px; font-weight: 600; }
  .nav-links li.active { background: var(--nav-active); }
  .search-box { position: absolute; right: 21px; top: 6px; width: 221px; height: 31px; background: var(--white); color: #888; font-size: 17px; padding: 3px 6px; }

  .hero { position: absolute; top: 186px; left: 0; width: 922px; height: 394px; background: linear-gradient(100deg, #3b2a22 0%, #d9a68a 28%, #f1d2bb 52%, #f6e7d4 70%, #e9d2a8 100%); }
  .hero-tagline { position: absolute; right: 50px; top: 44px; font-family: "Crimson Text", Georgia, serif; font-style: italic; font-size: 37px; line-height: 48px; text-align: center; color: var(--tagline); }

  .welcome { position: absolute; left: 44px; top: 626px; width: 480px; }
  .welcome h1 { font-size: 23px; font-weight: 600; color: var(--brand-blue); margin-bottom: 8px; }
  .welcome p { font-size: 14.5px; line-height: 19px; color: var(--text-soft); padding-left: 3px; margin-bottom: 19px; }
  .divider { position: absolute; left: 548px; top: 620px; height: 168px; border-left: 2px dotted #9a9a9a; }

  .testimonial { position: absolute; left: 584px; top: 608px; width: 292px; }
  .testimonial-head { display: flex; align-items: center; gap: 18px; }
  .testimonial-head h2 { font-size: 19.5px; font-weight: 400; color: var(--brand-blue); margin-top: 14px; }
  .quote { font-style: italic; font-size: 14px; line-height: 18.5px; color: var(--text-soft); margin-top: 6px; }
  .quote-author { margin-top: 12px; background: var(--navy-band); color: var(--white); font-size: 13.5px; padding: 4px 10px; line-height: 19px; position: relative; }
  .quote-author .view-all { position: absolute; right: 10px; bottom: 4px; }

  .listen { position: absolute; left: 46px; top: 818px; width: 840px; }
  .listen h2 { font-size: 23px; font-weight: 600; color: var(--brand-blue); }
  .features { display: flex; margin-top: 12px; }
  .feature { width: 280px; }
  .feature h3 { font-size: 17px; font-weight: 400; color: var(--text); margin: 0 0 6px 4px; }
  .feature-body { display: flex; gap: 14px; margin-left: 5px; }
  .feature-thumb { width: 76px; height: 76px; flex: none; }
  .feature-text { font-size: 10px; line-height: 13.3px; color: var(--text-soft); font-weight: 300; width: 150px; }
  .feature-text a { color: var(--link-blue); text-decoration: none; font-weight: 400; }
  .thumb-1 { background: linear-gradient(135deg, #c7d4dc, #e9e2d8 55%, #a24a3a); }
  .thumb-2 { background: linear-gradient(135deg, #1f2a1c, #4d5a3a 60%, #2a2a2a); }
  .thumb-3 { background: linear-gradient(135deg, #a9b4bd, #3a2a22 55%, #1e2a3e); }

  .site-footer { position: absolute; left: 0; top: 1033px; width: 922px; }
  .footer-col { position: absolute; top: 0; font-size: 13.5px; line-height: 17px; color: var(--text-soft); }
  .footer-col h4 { font-size: 13.5px; font-weight: 400; color: var(--link-blue); margin-bottom: 4px; text-transform: uppercase; }
  .footer-col ul { list-style: none; padding-left: 2px; }
  .social { position: absolute; right: 48px; top: 117px; display: flex; gap: 10px; }
  .social span { width: 24px; height: 24px; border-radius: 50%; background: var(--icon-grey); display: block; }
  .copyright { position: absolute; top: 1173px; width: 922px; text-align: center; font-size: 12px; color: var(--text-soft); }
</style>
</head>
<body>

<header class="site-header">
  <div class="brand">
    <div class="brand-name">
      <span class="line-1">Tarvin Grove</span>
      <span class="line-2">MEDICAL CENTRE</span>
    </div>
    <span class="brand-mark"></span>
  </div>

  <div class="contact-list">
    <div class="contact-item">
      <svg width="18" height="20" viewBox="0 0 18 20"><path d="M4 1 L7 5 L5 8 C6 11 8 13 10 14 L13 12 L17 15 L15 19 C8 18 2 12 1 4 Z" fill="#333"/></svg>
      <span>Phone: (08) 9371 4820</span>
    </div>
    <div class="contact-item">
      <svg width="22" height="22" viewBox="0 0 22 22"><circle cx="11" cy="11" r="11" fill="#333"/><text x="11" y="15.5" font-size="13" font-weight="700" fill="#fff" text-anchor="middle" font-family="Arial, sans-serif">@</text></svg>
      <span>Email: hello@tarvingrove.net.au</span>
    </div>
    <div class="contact-item">
      <svg width="26" height="18" viewBox="0 0 26 18"><rect x="1" y="1" width="24" height="16" fill="none" stroke="#333" stroke-width="2"/><path d="M1 1 L13 10 L25 1" fill="none" stroke="#333" stroke-width="2"/></svg>
      <span>U 14 / 108 Harbour Rise Blvd, Lindale WA 6041</span>
    </div>
    <div class="hours">
      <span class="hours-label">Opening Hours</span>
      <span class="hours-today">TODAY &nbsp; 8:00am - 6.00pm</span>
    </div>
  </div>
</header>

<nav class="main-nav">
  <ul class="nav-links">
    <li class="active">Home Page</li>
    <li>Practice Staff</li>
    <li>Services We Offer</li>
    <li>Information</li>
    <li>Facilities</li>
    <li>Contact Us</li>
  </ul>
  <div class="search-box">Search</div>
</nav>

<section class="hero" role="img" aria-label="Warm photograph of a mother holding and kissing her baby">
  <p class="hero-tagline">A practice<br>for all your<br>general needs.</p>
</section>

<section class="welcome">
  <h1>Welcome to Tarvin Grove Medical Centre</h1>
  <p>Lorem ipsum dolor sit amet, consectetur adipiscing elit. Duis rutrum dignissim ligula malesuada lobortis. Integer eros dui.</p>
  <p>Sollicitudin vel adipiscing vitae, semper in elit. Vivamus rhoncus nulla libero, at lobortis nibh. Mauris sit amet turpis in ante cursus adipiscing. Sed dui nulla, eleifend vel imperdiet eu.</p>
</section>

<div class="divider"></div>

<aside class="testimonial">
  <div class="testimonial-head">
    <svg width="70" height="46" viewBox="0 0 70 46">
      <path d="M2 2 H40 V28 H16 L8 36 V28 H2 Z" fill="#fff" stroke="#1558a8" stroke-width="2"/>
      <path d="M24 10 H68 V36 H62 V44 L54 36 H24 Z" fill="#fff" stroke="#1558a8" stroke-width="2"/>
    </svg>
    <h2>What Our Patients Say:</h2>
  </div>
  <p class="quote">&ldquo;Lorem ipsum dolor sit amet, consectetur adipiscing elit. Duis rutrum dignissim ligula malesuada lobortis. Integer eros dui. Viv mus rhoncus nulla ante cursus adipiscing. &rdquo;</p>
  <div class="quote-author">
    Marcus Hale<br>Director | Brookfield Care
    <span class="view-all">+ View All</span>
  </div>
</aside>

<section class="listen">
  <h2>We take the time to listen.</h2>
  <div class="features">
    <article class="feature">
      <h3>Lorem ipsum dolor sit amet.</h3>
      <div class="feature-body">
        <div class="feature-thumb thumb-1" role="img" aria-label="Doctor consulting with a patient"></div>
        <p class="feature-text">Lorem ipsum dolor sit amet, consectetur adipiscing elit. Duis rutrum dignissim ligula malesuada lobortis. Integer eros dui, sollicitudin vel adipiscing vitae, semper in elit. Vivamus rhoncus nulla libero. Duis rutrum. <a href="#">READ MORE</a></p>
      </div>
    </article>
    <article class="feature">
      <h3>Lorem ipsum dolor sit amet.</h3>
      <div class="feature-body">
        <div class="feature-thumb thumb-2" role="img" aria-label="Woman jogging outdoors"></div>
        <p class="feature-text">Lorem ipsum dolor sit amet, consectetur adipiscing elit. Duis rutrum dignissim ligula malesuada lobortis. Integer eros dui, sollicitudin vel adipiscing vitae, semper in elit. Vivamus rhoncus nulla libero. Duis rutrum. <a href="#">READ MORE</a></p>
      </div>
    </article>
    <article class="feature">
      <h3>Lorem ipsum dolor sit amet.</h3>
      <div class="feature-body">
        <div class="feature-thumb thumb-3" role="img" aria-label="Smiling man in a suit"></div>
        <p class="feature-text">Lorem ipsum dolor sit amet, consectetur adipiscing elit. Duis rutrum dignissim ligula malesuada lobortis. Integer eros dui, sollicitudin vel adipiscing vitae, semper in elit. Vivamus rhoncus nulla libero. Duis rutrum. <a href="#">READ MORE</a></p>
      </div>
    </article>
  </div>
</section>

<footer class="site-footer">
  <div class="footer-col" style="left:47px"><h4>Home Page</h4><ul><li>Lorem</li><li>Ipsum</li><li>Sit amet</li><li>Duis rutrum</li></ul></div>
  <div class="footer-col" style="left:170px"><h4>Practice Staff</h4><ul><li>Lorem</li><li>Ipsum</li><li>Sit amet</li><li>Duis rutrum</li></ul></div>
  <div class="footer-col" style="left:290px"><h4>Services We Offer</h4><ul><li>Lorem</li><li>Ipsum</li><li>Sit amet</li><li>Duis rutrum</li></ul></div>
  <div class="footer-col" style="left:446px"><h4>Information</h4><ul><li>Lorem</li><li>Ipsum</li><li>Sit amet</li><li>Duis rutrum</li></ul></div>
  <div class="footer-col" style="left:583px"><h4>Facilities</h4><ul><li>Dr. Lorem</li><li>Dr. Ipsum</li><li>Dr. Sit amet</li><li>Dr. Duis rutrum</li></ul></div>
  <div class="footer-col" style="left:696px"><h4>Contact Us</h4><ul><li>U 14 / 108 Harbour Rise Blvd,</li><li>Lindale WA 6041</li><li>TEL. (08) 9371 4820</li><li>Email:hello@tarvingrove.net.au</li></ul></div>
  <div class="social" aria-label="Social links"><span></span><span></span><span></span></div>
</footer>

<p class="copyright">All Content © Tarvin Grove Medical Centre. All Rights Reserved.</p>

</body>
</html>
```